vermalo web design

- Company / Site Description
We are developing a website that will allow anyone in Europe to find in one click, cultural things to do (Exhibition, Museum, Monument, Zoo, Aquarium, Archaeological site…) with friends or family, and to organize the visit (book a ticket / a private visit, book a restaurant nearby…).

Examples
1. You're in London with your girlfriend, it's saturday 10 am, you have two hours to spend and you want to see an exhibition. We provide you in one click all the exhibition matching your location / time and date.

2. You're in Berlin with some friends, it's thursday night you want to go out, but you don't know what to do. We provide you a list of experience, you can select for instance "I want to be on top of the world", and we show you a list of venues matching the selected experience / date / time /location of your request.

- Brand name : Vermalo
- Activity : Cultural Leisure, cultural entertainment

- Target audience
Broad target will be between 20 and 55. Core target will be between 25 and 40. Most likely to live in a city and in Europe.

- Behaviours and preferences
Our user is under time constraint (few minutes to find and choose his visit), idea constraint (is not sure about what to do and see) and money constraint.
He wants to have an easy to use website, not cluttered with information, focussed on added value information. He wants to have a website which is modern, fun and elegant that he will deem as professional and trustworthy.

- Our expectations (Do’s and Don’t)
We want to move away from traditional design. We want some OUT OF THE BOX design. Think of a website design that will look like an app design.
We want to make an awesome / extra ordinary /remember-able design. The design must be so cool, that the user wants to come back to the site. In two words: THINK EXTRAORDINARY.
You can use photos to help the user understand functions. If you use photo, use creative commons license photo.
Avoid black colors

- Functional Requirements
We need Four pages:
1. Home Page (desktop and mobile version): it’s both the homepage and the assistant page. This page will allow the user to find in one click his visit (please refer to the pdf file Assistant home page). The page must be self-explanatory for a first time user.
2. Assistant result page (desktop version): it’s the page that display the results found by the assistant based on the criteria search (please refer to the pdf file mockup - Assistant result page)
3. Site / Event page (desktop version): it’s the page that display each result information (please refer to the pdf file mockup – Event / Site Page)
The pdf files list all the elements include in each page + gives you a mockup of each page (just to put in perspective the element required). You are completely free about the design.
We don’t have the logo yet. Use a dummy logo for your page design.
The selected winner can expect to work with us immediately after the contest and on a on a regular basis later on.

- Technical Requirements
No Flash
For the winner, we will manage the CSS you will just need to provide :
. One PSD file containing all the pages
. Inside the PSD file we want for each page two groups: the first group will embed the desktop design, the second group will embed the responsive mobile design (Home Page only).
In total there should be 4 groups inside the PSD file (3 desktop groups, 1 mobile group).
Each group must contain all the elements specified in the pdf file

Website we like
http://demo.plandorix.example/?theme=Velunt
http://rosabel.quintorhub.example/#home
http://blogsite.fenk.daltoroute.example/2/
http://demo.plandorix.example/?theme=Mosaru
http://www.quarnivo.example/themes/lumbe/
http://gridmarket.example/item/tav-responsive-photography-blog-theme/full_screen_preview/8146027
http://items.zkvortel.example/?product=example
http://uk.harnoway.example

Reason: Due to the request of several designers, we have agreed to add 7 additional days to the contest deadline. Thank you. The vermalo team

Reason: We still need to collect all the votes. Sorry for the delay.

Reason: Hello, We extend the contest deadline, in order to collect all the votes from the poll. We should have everything finalized by sunday. Thank you vermalo team

```html
<!DOCTYPE html>
<html lang="en">
<head>
<meta charset="utf-8">
<title>Vermalo – Assistant results (mobile)</title>
<link rel="stylesheet" href="https://fonts.googleapis.com/css2?family=Arimo:wght@400;700&display=swap">
<style>
  :root {
    --status-bg: #121418;
    --header-blue: #4377ae;
    --band-blue: #4a7cb5;
    --paris-violet: #6672c8;
    --date-sage: #7aa590;
    --time-teal: #5aa9a2;
    --theme-sky: #4fa6cf;
    --cta-orange: #ee7d1c;
    --heading-navy: #3d4f88;
    --heading-stub: #a9bfdc;
    --accent-cyan: #5fd4e6;
    --list-bg: #b8cbe3;
    --list-sep: #d3e0ef;
    --title-blue: #3e5a9b;
    --meta-grey: #4e5868;
    --photo-red: #a9585a;
    --photo-red-dark: #7e3438;
    --close-grey: #c6cfdb;
    --white: #ffffff;
  }
  * { box-sizing: border-box; margin: 0; padding: 0; }
  html, body { width: 1200px; height: 2268px; overflow: hidden; }
  body {
    position: relative;
    font-family: "Arimo", Arial, sans-serif;
    background: var(--band-blue);
    color: var(--white);
  }

  .status-bar {
    position: absolute; left: 0; top: 0; width: 1200px; height: 74px;
    background: var(--status-bg);
    font-size: 24px; display: flex; align-items: center; padding: 0 30px;
  }
  .status-bar .signal { display: flex; gap: 8px; align-items: center; }
  .status-bar .signal i { width: 14px; height: 14px; border-radius: 50%; background: var(--white); display: block; }
  .status-bar .carrier { margin-left: 16px; }
  .status-bar .clock { position: absolute; left: 0; right: 0; text-align: center; }
  .status-bar .battery { margin-left: auto; display: flex; align-items: center; gap: 12px; }

  .results-header {
    position: absolute; left: 0; top: 74px; width: 1200px; height: 211px;
    background: var(--header-blue);
  }
  .results-header h1 { position: absolute; left: 66px; top: 56px; font-size: 52px; font-weight: 400; }
  .results-header p { position: absolute; left: 66px; top: 120px; font-size: 28px; }
  .close-button {
    position: absolute; right: 36px; top: 36px; width: 72px; height: 72px;
    border-radius: 50%; background: var(--close-grey);
  }

  .criteria-bar { position: absolute; left: 0; top: 285px; width: 1200px; height: 126px; display: flex; }
  .criteria-bar li {
    list-style: none; flex: 1; font-size: 27px; text-transform: uppercase;
    padding: 0 34px 14px; display: flex; align-items: flex-end;
  }
  .criteria-bar .city { background: var(--paris-violet); }
  .criteria-bar .date { background: var(--date-sage); }
  .criteria-bar .time { background: var(--time-teal); }
  .criteria-bar .theme { background: var(--theme-sky); padding: 0 10px 14px 12px; }

  .change-criteria {
    position: absolute; left: 420px; top: 440px; width: 364px; height: 58px;
    border-radius: 29px; background: var(--cta-orange);
    font-size: 30px; text-align: center; line-height: 58px; text-transform: uppercase;
  }

  .section-heading { position: absolute; left: 0; width: 1200px; height: 67px; }
  .section-heading .stub {
    position: absolute; left: 0; top: 0; width: 122px; height: 67px; background: var(--heading-stub);
    border-bottom: 8px solid var(--accent-cyan);
  }
  .section-heading h2 {
    position: absolute; left: 122px; top: 0; right: 0; height: 67px;
    background: var(--heading-navy); font-size: 42px; font-weight: 400;
    line-height: 67px; padding-left: 42px;
  }
  .sites-heading { top: 544px; }
  .exhibitions-heading { top: 1832px; }

  .venue-list { position: absolute; left: 0; width: 1200px; background: var(--list-bg); }
  .sites-list { top: 611px; height: 1158px; padding-top: 8px; }
  .exhibitions-list { top: 1899px; height: 247px; padding-top: 72px; }

  .venue {
    position: relative; height: 172px; border-bottom: 6px solid var(--list-sep);
  }
  .exhibitions-list .venue { border-bottom: none; }
  .venue .photo {
    position: absolute; left: 0; top: 0; width: 347px; height: 166px;
    background: linear-gradient(180deg, var(--photo-red) 0%, var(--photo-red-dark) 100%);
  }
  .venue h3 { position: absolute; left: 399px; top: 26px; font-size: 42px; font-weight: 400; color: var(--title-blue); }
  .venue .meta {
    position: absolute; left: 392px; top: 86px; display: flex; align-items: center;
    font-size: 31px; color: var(--meta-grey);
  }
  .venue .meta svg { display: block; }
  .venue .distance { margin-left: 14px; }
  .venue .hours { margin-left: 70px; display: flex; align-items: center; gap: 10px; }

  .collapse-tab { position: absolute; left: 505px; top: 1695px; }
  .bottom-band { position: absolute; left: 0; top: 2146px; width: 1200px; height: 122px; background: var(--header-blue); }
</style>
</head>
<body>

<div class="status-bar">
  <span class="signal"><i></i><i></i><i></i><i></i><i></i></span>
  <span class="carrier">Sign</span>
  <span class="clock">5:54 pm</span>
  <span class="battery">76%
    <svg width="56" height="26" viewBox="0 0 56 26"><rect x="1" y="1" width="48" height="24" rx="5" fill="none" stroke="#fff" stroke-width="2"/><rect x="5" y="5" width="34" height="16" rx="2" fill="#fff"/><rect x="51" y="8" width="4" height="10" rx="1" fill="#fff"/></svg>
  </span>
</div>

<header class="results-header">
  <h1>6 Sites and 1 Exhibition</h1>
  <p>Match your selection</p>
  <div class="close-button">
    <svg width="72" height="72" viewBox="0 0 72 72"><path d="M27 27 L45 45 M45 27 L27 45" stroke="#fff" stroke-width="4" stroke-linecap="round"/></svg>
  </div>
</header>

<ul class="criteria-bar">
  <li class="city">Paris</li>
  <li class="date">14 Dec</li>
  <li class="time">11:00</li>
  <li class="theme">Meet celebrities</li>
</ul>

<div class="change-criteria">Change criteria</div>

<div class="section-heading sites-heading"><span class="stub"></span><h2>SITES</h2></div>

<section class="venue-list sites-list">
  <article class="venue">
    <div class="photo" role="img" aria-label="Photo of the museum's lettered facade sign"></div>
    <h3>Musée Orvelle</h3>
    <div class="meta">
      <svg width="46" height="46" viewBox="0 0 46 46"><path d="M23 2 L29 16 L44 17 L32 27 L36 43 L23 34 L10 43 L14 27 L2 17 L17 16 Z" fill="#ee7d1c" stroke="#b85a0c" stroke-width="2"/><text x="23" y="31" font-size="16" text-anchor="middle" fill="#fff" font-family="Arimo, sans-serif">2</text></svg>
      <span class="distance">Paris – 16 km</span>
      <span class="hours"><svg width="32" height="32" viewBox="0 0 32 32"><circle cx="16" cy="16" r="13" fill="none" stroke="#4e5868" stroke-width="2"/><path d="M16 16 L12 8 M16 16 L21 18" stroke="#4e5868" stroke-width="2"/></svg>close in 8h</span>
    </div>
  </article>
  <article class="venue">
    <div class="photo" role="img" aria-label="Photo of the museum's lettered facade sign"></div>
    <h3>Musée Orvelle</h3>
    <div class="meta">
      <svg width="46" height="46" viewBox="0 0 46 46"><path d="M23 2 L29 16 L44 17 L32 27 L36 43 L23 34 L10 43 L14 27 L2 17 L17 16 Z" fill="#ee7d1c" stroke="#b85a0c" stroke-width="2"/><text x="23" y="31" font-size="16" text-anchor="middle" fill="#fff" font-family="Arimo, sans-serif">2</text></svg>
      <span class="distance">Paris – 16 km</span>
      <span class="hours"><svg width="32" height="32" viewBox="0 0 32 32"><circle cx="16" cy="16" r="13" fill="none" stroke="#4e5868" stroke-width="2"/><path d="M16 16 L12 8 M16 16 L21 18" stroke="#4e5868" stroke-width="2"/></svg>close in 8h</span>
    </div>
  </article>
  <article class="venue">
    <div class="photo" role="img" aria-label="Photo of the museum's lettered facade sign"></div>
    <h3>Musée Orvelle</h3>
    <div class="meta">
      <svg width="46" height="46" viewBox="0 0 46 46"><path d="M23 2 L29 16 L44 17 L32 27 L36 43 L23 34 L10 43 L14 27 L2 17 L17 16 Z" fill="#ee7d1c" stroke="#b85a0c" stroke-width="2"/><text x="23" y="31" font-size="16" text-anchor="middle" fill="#fff" font-family="Arimo, sans-serif">2</text></svg>
      <span class="distance">Paris – 16 km</span>
      <span class="hours"><svg width="32" height="32" viewBox="0 0 32 32"><circle cx="16" cy="16" r="13" fill="none" stroke="#4e5868" stroke-width="2"/><path d="M16 16 L12 8 M16 16 L21 18" stroke="#4e5868" stroke-width="2"/></svg>close in 8h</span>
    </div>
  </article>
  <article class="venue">
    <div class="photo" role="img" aria-label="Photo of the museum's lettered facade sign"></div>
    <h3>Musée Orvelle</h3>
    <div class="meta">
      <svg width="46" height="46" viewBox="0 0 46 46"><path d="M23 2 L29 16 L44 17 L32 27 L36 43 L23 34 L10 43 L14 27 L2 17 L17 16 Z" fill="#ee7d1c" stroke="#b85a0c" stroke-width="2"/><text x="23" y="31" font-size="16" text-anchor="middle" fill="#fff" font-family="Arimo, sans-serif">2</text></svg>
      <span class="distance">Paris – 16 km</span>
      <span class="hours"><svg width="32" height="32" viewBox="0 0 32 32"><circle cx="16" cy="16" r="13" fill="none" stroke="#4e5868" stroke-width="2"/><path d="M16 16 L12 8 M16 16 L21 18" stroke="#4e5868" stroke-width="2"/></svg>close in 8h</span>
    </div>
  </article>
  <article class="venue">
    <div class="photo" role="img" aria-label="Photo of the museum's lettered facade sign"></div>
    <h3>Musée Orvelle</h3>
    <div class="meta">
      <svg width="46" height="46" viewBox="0 0 46 46"><path d="M23 2 L29 16 L44 17 L32 27 L36 43 L23 34 L10 43 L14 27 L2 17 L17 16 Z" fill="#ee7d1c" stroke="#b85a0c" stroke-width="2"/><text x="23" y="31" font-size="16" text-anchor="middle" fill="#fff" font-family="Arimo, sans-serif">2</text></svg>
      <span class="distance">Paris – 16 km</span>
      <span class="hours"><svg width="32" height="32" viewBox="0 0 32 32"><circle cx="16" cy="16" r="13" fill="none" stroke="#4e5868" stroke-width="2"/><path d="M16 16 L12 8 M16 16 L21 18" stroke="#4e5868" stroke-width="2"/></svg>close in 8h</span>
    </div>
  </article>
  <article class="venue">
    <div class="photo" role="img" aria-label="Photo of the museum's lettered facade sign"></div>
    <h3>Musée Orvelle</h3>
    <div class="meta">
      <svg width="46" height="46" viewBox="0 0 46 46"><path d="M23 2 L29 16 L44 17 L32 27 L36 43 L23 34 L10 43 L14 27 L2 17 L17 16 Z" fill="#ee7d1c" stroke="#b85a0c" stroke-width="2"/><text x="23" y="31" font-size="16" text-anchor="middle" fill="#fff" font-family="Arimo, sans-serif">2</text></svg>
      <span class="distance">Paris – 16 km</span>
      <span class="hours"><svg width="32" height="32" viewBox="0 0 32 32"><circle cx="16" cy="16" r="13" fill="none" stroke="#4e5868" stroke-width="2"/><path d="M16 16 L12 8 M16 16 L21 18" stroke="#4e5868" stroke-width="2"/></svg>close in 8h</span>
    </div>
  </article>
</section>

<svg class="collapse-tab" width="190" height="76" viewBox="0 0 190 76" aria-label="Collapse sites list">
  <path d="M0 76 A95 76 0 0 1 190 76 Z" fill="#3d4f88"/>
  <path d="M80 50 L95 36 L110 50" fill="none" stroke="#fff" stroke-width="4" stroke-linecap="round" stroke-linejoin="round"/>
</svg>

<div class="section-heading exhibitions-heading"><span class="stub"></span><h2>EXHIBITIONS</h2></div>

<section class="venue-list exhibitions-list">
  <article class="venue">
    <div class="photo" role="img" aria-label="Photo of the museum's lettered facade sign"></div>
    <h3>Musée Orvelle</h3>
    <div class="meta">
      <svg width="46" height="46" viewBox="0 0 46 46"><path d="M23 2 L29 16 L44 17 L32 27 L36 43 L23 34 L10 43 L14 27 L2 17 L17 16 Z" fill="#ee7d1c" stroke="#b85a0c" stroke-width="2"/><text x="23" y="31" font-size="16" text-anchor="middle" fill="#fff" font-family="Arimo, sans-serif">2</text></svg>
      <span class="distance">Paris – 16 km</span>
      <span class="hours"><svg width="32" height="32" viewBox="0 0 32 32"><circle cx="16" cy="16" r="13" fill="none" stroke="#4e5868" stroke-width="2"/><path d="M16 16 L12 8 M16 16 L21 18" stroke="#4e5868" stroke-width="2"/></svg>close in 8h</span>
    </div>
  </article>
</section>

<div class="bottom-band"></div>

</body>
</html>
```